Flyer Design Project

We need a flyer for a new company in the UK. We are selling parcels against Ashbury Post, new exciting venture with better pricing and more convenience than the standard postal offering. Our colors are green and white and blue check out our website www.tundrivexa.com

We want to highlight our convenience and savings...

Target Market(s)

Normally expat living in the UK sending parcels home

Industry/Entity Type

It Company

```html
<!DOCTYPE html>
<html lang="en">
<head>
<meta charset="utf-8">
<title>Tundrivexa – Low Cost International Parcel Delivery</title>
<link rel="stylesheet" href="https://fonts.googleapis.com/css2?family=Arimo:wght@400;700&family=Archivo+Black&family=Roboto+Condensed:wght@700&family=Open+Sans:wght@400&display=swap">
<style>
  :root {
    --green: #4cb648;
    --green-dark: #3f9e45;
    --grey-text: #5e5f61;
    --grey-band-light: #d4d5d7;
    --grey-band-dark: #7a7b7e;
    --paper: #f3f5f8;
    --ink: #1d1d1f;
    --intro-ink: #3a3b3d;
    --white: #ffffff;
    --blue: #2f6fc0;
  }
  * { margin: 0; padding: 0; box-sizing: border-box; }
  html, body { width: 960px; height: 1200px; overflow: hidden; }
  body {
    background: var(--paper);
    font-family: "Arimo", Arial, sans-serif;
    color: var(--ink);
  }
  .flyer {
    position: relative;
    width: 960px;
    height: 1200px;
    overflow: hidden;
    background: linear-gradient(180deg, #f7f8fb 0%, #eef1f5 100%);
  }
  .header-band { position: absolute; left: 0; top: 0; width: 960px; height: 320px; }
  .headline {
    position: absolute; top: 20px; left: 0; width: 960px;
    text-align: center; color: var(--white); white-space: nowrap;
  }
  .headline .small { font-size: 24px; letter-spacing: 1.5px; font-weight: 700; }
  .headline .large { font-size: 40px; font-weight: 700; letter-spacing: 0.5px; }

  .brand { position: absolute; left: 40px; top: 160px; display: flex; align-items: center; }
  .brand-dot {
    width: 140px; height: 140px; border-radius: 50%;
    background: var(--blue);
  }
  .brand-name {
    margin-left: 24px;
    font-size: 68px; font-weight: 700; letter-spacing: -2px;
    color: var(--grey-text);
  }
  .tagline {
    position: absolute; right: 210px; top: 264px;
    font-family: "Roboto Condensed", Arial, sans-serif;
    font-size: 32px; font-weight: 700; color: var(--grey-text);
  }

  .phone {
    position: absolute; left: 320px; top: 338px;
    display: flex; align-items: center;
    font-size: 54px; font-weight: 700; color: var(--grey-text);
  }
  .phone svg { width: 38px; height: 42px; margin-right: 18px; }

  .intro {
    position: absolute; left: 320px; top: 430px;
    font-size: 37px; line-height: 44px; font-weight: 400; color: var(--intro-ink);
  }
  .intro strong { font-weight: 700; color: var(--grey-text); }
  .intro .brand-word { color: var(--green); font-weight: 700; }

  .rocket {
    position: absolute; left: 44px; top: 440px; width: 292px; height: 480px;
    border-radius: 146px 146px 20px 20px;
    background: radial-gradient(ellipse at 50% 45%, #5b9be0 0%, #2a63b3 55%, #dfe6ef 100%);
  }

  .steps { position: absolute; left: 322px; top: 548px; width: 590px; }
  .step-title {
    display: flex; align-items: center;
    font-size: 30px; font-weight: 700; color: var(--green);
    letter-spacing: 0.5px;
  }
  .step-bullet {
    width: 26px; height: 26px; border-radius: 50%;
    background: var(--blue); margin-right: 14px; flex: none;
  }
  .step-text {
    margin-left: 40px; width: 550px;
    font-size: 20px; line-height: 23px; color: var(--ink);
  }
  .step--print { margin-top: 26px; }
  .step--send { margin-top: 30px; }
  .step--send .step-text { text-align: justify; }

  .savings {
    position: absolute; left: 44px; top: 972px;
    font-family: "Archivo Black", Arial, sans-serif;
    font-size: 55px; line-height: 64px; color: var(--grey-text);
    letter-spacing: 0.5px;
  }
  .savings .accent { color: var(--green); }

  .rule { position: absolute; left: 0; top: 1106px; width: 960px; height: 4px; background: #8b8c8f; }
  .footer {
    position: absolute; left: 0; top: 1116px; width: 960px; height: 84px;
    background: var(--green-dark); color: var(--white);
    font-family: "Open Sans", Arial, sans-serif; font-size: 23px; line-height: 33px;
    text-align: center; padding-top: 10px;
  }
</style>
</head>
<body>
<main class="flyer">
  <svg class="header-band" viewBox="0 0 960 320" aria-hidden="true">
    <defs>
      <linearGradient id="band-grey" x1="0" y1="0" x2="1" y2="0">
        <stop offset="0" stop-color="#d4d5d7"/>
        <stop offset="1" stop-color="#7a7b7e"/>
      </linearGradient>
    </defs>
    <rect width="960" height="320" fill="url(#band-grey)"/>
    <path d="M0,138 Q440,10 960,240 L960,320 L0,320 Z" fill="#f6f7fa"/>
    <path d="M0,140 Q440,12 960,242" fill="none" stroke="#4cb648" stroke-width="18"/>
    <path d="M0,122 Q280,60 520,80" fill="none" stroke="#ffffff" stroke-width="4"/>
  </svg>

  <h1 class="headline"><span class="small">LOW COST INTERNATIONAL</span> <span class="large">PARCEL DELIVERY</span></h1>

  <div class="brand">
    <span class="brand-dot"></span>
    <span class="brand-name">Tundrivexa</span>
  </div>
  <p class="tagline">Pack. Send. Relax.</p>

  <p class="phone">
    <svg viewBox="0 0 24 26" aria-hidden="true"><path d="M6 2 L9 2 L11 8 L8 10 Q10 16 15 19 L17 16 L23 18 L23 22 Q22 25 18 24 Q4 19 2 6 Q2 2 6 2 Z" fill="#5e5f61"/></svg>
    01632 960418
  </p>

  <h2 class="intro">Three easy steps to launching<br><span class="brand-word">Tundrivexa</span> <strong>service</strong></h2>

  <div class="rocket" role="img" aria-label="Glossy blue cartoon rocket standing upright on its fins"></div>

  <section class="steps">
    <div class="step step--select">
      <h3 class="step-title"><span class="step-bullet"></span>Select</h3>
      <p class="step-text">Simply log-on, "Select" the service you require, enter in your important parcel information and complete the payment process.</p>
    </div>
    <div class="step step--print">
      <h3 class="step-title"><span class="step-bullet"></span>Print</h3>
      <p class="step-text">Print and affix your shipping label to the parcel.</p>
    </div>
    <div class="step step--send">
      <h3 class="step-title"><span class="step-bullet"></span>Send - You’re ready to launch!</h3>
      <p class="step-text">Simply drop off your parcel at any one of over 4500 convenient outlets, some of which are open early until late, 7 days a week. From there, it is sent directly to one of our processing centres where your parcel is checked and prepared for its international journey.</p>
    </div>
  </section>

  <p class="savings">SAVE UP TO <span class="accent">60%</span> ON<br>INTERNATIONAL PARCELS</p>

  <div class="rule"></div>
  <footer class="footer">
    Unit 4, Fenwell Trade Park, Harlow Vale, Hartshire, HV2 9QT<br>
    Email: cs@tundrivexa.com
  </footer>
</main>
</body>
</html>
```